Marlow Cybersecurity Secives professional web site

Marlow is a unit of the Tesselcore company, based on the audit services it offers and which mainly works by the contacts it has from its previous experience. The objective with the development of this website will be to increase its presence on the internet and even link the traffic of its social networks with the blog of the new page and in this way, provide information for old and potential customers.
For this reason, we will set the objective of the page, have all the information of the company, its services and its scope in general, in a formal and simple for users, facilitating the task of finding the information they want within of the page, as well as, including the option of feedback.

Target Market(s)

any company that needs security assessments

Number of Pages Required

4 page

Font styles to use
Sans Serif

Colors

Designer to choose colors to be used in the design.

Requirements
Must have
• READ THE PDF PLEASE. Video in homepage, cool graphics, color like our logo
• I like the following sites: www.tesselcore-example.com & www.quarbitex-example.com
Nice to have
• Futuristic
Should not have
• Please, dont use the gallery pictures I used in my document, I prefer hand made illustrations instead

```html
<!DOCTYPE html>
<html lang="en">
<head>
<meta charset="utf-8">
<title>Marlow Security — Experts in Cybersecurity</title>
<link rel="stylesheet" href="https://fonts.googleapis.com/css2?family=Raleway:wght@400;600;700;800&display=swap">
<style>
  :root {
    --navy-deep: #050a30;
    --navy: #0a1a5c;
    --royal: #0d3fa8;
    --cyan: #1fe3f5;
    --cyan-dot: #22d8ee;
    --dot-idle: #4a5a9a;
    --white: #ffffff;
    --divider: #1c2350;
    --video-bg: #04062a;
  }
  * { margin: 0; padding: 0; box-sizing: border-box; }
  html, body { width: 1200px; height: 670px; overflow: hidden; background: var(--navy-deep); }
  body { font-family: "Raleway", Arial, sans-serif; color: var(--white); position: relative; }

  .site-header {
    position: absolute; left: 0; top: 0; width: 1200px; height: 67px;
    background: var(--navy-deep);
  }
  .brand {
    position: absolute; left: 162px; top: 17px;
    display: flex; align-items: center; gap: 8px;
  }
  .brand-name {
    font-weight: 800; font-size: 15px; line-height: 13px; text-align: right;
    letter-spacing: 0.2px;
  }
  .brand-mark { width: 30px; height: 30px; border-radius: 50%; background: var(--white); }

  .main-nav {
    position: absolute; top: 27px; left: 0; width: 100%;
    font-weight: 700; font-size: 13.6px; letter-spacing: 0.2px;
  }
  .main-nav a { position: absolute; color: var(--white); text-decoration: none; }
  .nav-home { left: 584px; }
  .nav-services { left: 665px; }
  .nav-blog { left: 771px; }
  .nav-contact { left: 850px; }

  .nav-divider {
    position: absolute; left: 931px; top: 4px; width: 1px; height: 58px;
    background: var(--divider);
  }
  .language {
    position: absolute; top: 16px; width: 50px; text-align: center;
    font-size: 9.6px; font-weight: 400;
  }
  .language-en { left: 951px; }
  .language-es { left: 997px; }
  .language-flag {
    display: block; width: 28px; height: 28px; border-radius: 50%;
    margin: 0 auto 3px;
  }
  .language-en .language-flag { background: radial-gradient(circle, #d8232a 0 30%, #ffffff 31% 45%, #1f3c8c 46%); }
  .language-es .language-flag { background: linear-gradient(#c8102e 0 25%, #f6c500 25% 75%, #c8102e 75%); }

  .hero {
    position: absolute; left: 0; top: 67px; width: 1200px; height: 527px;
  }
  .hero-art {
    position: absolute; inset: 0;
    background:
      radial-gradient(ellipse 380px 300px at 560px 230px, rgba(30,110,220,0.55), transparent 70%),
      linear-gradient(90deg, #041040 0%, #06206e 30%, #0b4fb8 62%, #1590dc 82%, var(--cyan) 100%);
  }
  .hero-title {
    position: absolute; left: 160px; top: 111px; width: 420px;
    font-weight: 800; font-size: 34.5px; line-height: 46px; text-transform: uppercase;
  }
  .slider-dots {
    position: absolute; left: 161px; top: 439px; display: flex; gap: 1.5px;
  }
  .slider-dot { width: 13.5px; height: 13.5px; border-radius: 50%; background: var(--dot-idle); }
  .slider-dot.is-active { background: var(--cyan-dot); }

  .video {
    position: absolute; left: 622px; top: 75px; width: 523px; height: 338px;
    background: var(--video-bg);
  }
  .video-art {
    position: absolute; inset: 0;
    background:
      radial-gradient(circle 100px at 380px 166px, #2a6fd6 0%, #123a9a 60%, rgba(10,30,110,0.3) 100%),
      linear-gradient(180deg, transparent 40%, rgba(20,80,180,0.35) 50%, transparent 60%),
      var(--video-bg);
  }
  .video-play { position: absolute; left: 209px; top: 117px; }

  .site-footer {
    position: absolute; left: 0; top: 594px; width: 1200px; height: 76px;
    background: var(--navy-deep);
  }
  .social-links { position: absolute; left: 162px; top: 34px; display: flex; font-size: 14px; }
  .social-link { display: flex; align-items: center; color: var(--white); text-decoration: none; margin-right: 30px; }
  .social-icon { width: 14px; height: 14px; background: var(--white); margin-right: 13px; }
  .social-icon.is-round { border-radius: 50%; margin-right: 7px; }
  .social-link-chirp .social-icon { border-radius: 50%; margin-right: 13px; }
  .legal {
    position: absolute; right: 163px; top: 32px; font-size: 13px;
  }
  .legal a { color: var(--white); text-decoration: none; }
</style>
</head>
<body>
  <header class="site-header">
    <div class="brand">
      <div class="brand-name">MARLOW<br>SECURITY</div>
      <span class="brand-mark"></span>
    </div>
    <nav class="main-nav">
      <a class="nav-home" href="#">HOME</a>
      <a class="nav-services" href="#">SERVICES</a>
      <a class="nav-blog" href="#">BLOG</a>
      <a class="nav-contact" href="#">CONTACT</a>
    </nav>
    <span class="nav-divider"></span>
    <a class="language language-en"><span class="language-flag"></span>English</a>
    <a class="language language-es"><span class="language-flag"></span>Spanish</a>
  </header>

  <section class="hero">
    <div class="hero-art" role="img" aria-label="Illustration of a world map with circuit lines and gears in deep blue tones"></div>
    <h1 class="hero-title">Experts in cybersecurity. Protect your digital asset. We audit your company. Excellent reputation</h1>
    <div class="slider-dots">
      <span class="slider-dot is-active"></span>
      <span class="slider-dot"></span>
      <span class="slider-dot"></span>
      <span class="slider-dot"></span>
    </div>
    <div class="video">
      <div class="video-art" role="img" aria-label="Video still of a glowing globe wrapped in streams of binary code"></div>
      <svg class="video-play" width="106" height="106" viewBox="0 0 106 106" aria-label="Play video">
        <circle cx="53" cy="53" r="50" fill="none" stroke="#ffffff" stroke-width="4"/>
        <path d="M40 32 L76 53 L40 74 Z" fill="none" stroke="#ffffff" stroke-width="4" stroke-linejoin="round"/>
      </svg>
    </div>
  </section>

  <footer class="site-footer">
    <div class="social-links">
      <a class="social-link social-link-chirp" href="#"><span class="social-icon"></span>Chirpline</a>
      <a class="social-link" href="#"><span class="social-icon"></span>Snapframe</a>
      <a class="social-link" href="#"><span class="social-icon is-round"></span>Blog</a>
    </div>
    <p class="legal">© 2018 All Rights Reserved.<a href="#">Privacy Policy</a> | <a href="#">Terms of Use</a></p>
  </footer>
</body>
</html>
```